Design for supplement packages

We are developing a new supplement brand are looking for a label, based on the design of our naturopath practice. It should include our logo, the basic colors are green, gold and white. www.haus-solvarin.de is the practices web site.

Target Market(s)

Europe and North America

Industry/Entity Type

Supplement

Font styles to use
Sans Serif

Colors
acd037
ffffff

Requirements
Should not have
• A too busy design. I like it simple and high class

```html
<!DOCTYPE html>
<html lang="en">
<head>
<meta charset="utf-8">
<title>Haus Solvarin – Vitamin K2 Label</title>
<link href="https://fonts.googleapis.com/css2?family=Barlow+Condensed:wght@300;400;500;600&family=Barlow+Semi+Condensed:wght@300;400;500&display=swap" rel="stylesheet">
<style>
  :root {
    --bg: #e8e9e9;
    --label-white: #ffffff;
    --green: #acd037;
    --green-deep: #8fa63a;
    --gold: #c9a227;
    --gold-light: #f2de7a;
    --gold-dark: #9a6f12;
    --brown: #6e6157;
    --ink: #1e1e1e;
  }
  html, body {
    margin: 0;
    padding: 0;
    width: 1200px;
    height: 960px;
    overflow: hidden;
    background: var(--bg);
  }
  .canvas {
    position: relative;
    width: 1200px;
    height: 960px;
  }
  .label {
    position: absolute;
    left: 160px;
    top: 70px;
    width: 880px;
    height: 820px;
    background: var(--label-white);
    overflow: hidden;
    font-family: "Barlow Condensed", sans-serif;
    color: var(--brown);
  }
  .label-art {
    position: absolute;
    inset: 0;
  }
  .brand {
    position: absolute;
    left: 90px;
    top: 92px;
    display: flex;
    align-items: center;
    gap: 18px;
  }
  .brand-dot {
    width: 58px;
    height: 58px;
    border-radius: 50%;
    background: var(--green);
  }
  .brand-name {
    font-family: "Barlow Semi Condensed", sans-serif;
    font-weight: 300;
    font-size: 54px;
    line-height: 1;
    color: var(--green-deep);
  }
  .product-title {
    position: absolute;
    left: 90px;
    top: 300px;
    width: 560px;
    white-space: nowrap;
  }
  .title-vitamin {
    font-weight: 300;
    font-size: 56px;
    letter-spacing: 5px;
  }
  .title-k2 {
    font-weight: 500;
    font-size: 100px;
    line-height: 0.8;
    margin-left: 8px;
  }
  .title-rule {
    position: absolute;
    left: 90px;
    top: 392px;
    width: 600px;
    height: 2px;
    background: var(--brown);
  }
  .title-form {
    position: absolute;
    left: 420px;
    top: 398px;
    width: 200px;
    text-align: right;
    font-weight: 400;
    font-size: 46px;
    letter-spacing: 4px;
  }
  .source {
    position: absolute;
    left: 90px;
    top: 498px;
    font-weight: 400;
    font-size: 36px;
    line-height: 1.1;
  }
  .dose {
    position: absolute;
    left: 90px;
    top: 540px;
    font-weight: 400;
    font-size: 48px;
    letter-spacing: 2px;
  }
  .free-claim {
    position: absolute;
    left: 670px;
    top: 506px;
    color: var(--ink);
    font-weight: 600;
    text-align: left;
    line-height: 1;
  }
  .free-claim .small {
    display: block;
    font-size: 25px;
    letter-spacing: 4px;
  }
  .free-claim .big {
    display: block;
    font-size: 44px;
    letter-spacing: 5px;
    font-weight: 500;
    margin-top: 2px;
  }
  .count-badge {
    position: absolute;
    left: 220px;
    top: 684px;
    width: 420px;
    height: 52px;
    border-radius: 26px;
    background: linear-gradient(90deg, var(--gold-light), #f7eb9d 50%, var(--gold-light));
    box-shadow: 0 0 0 2px var(--gold);
    display: flex;
    align-items: center;
    justify-content: center;
    font-weight: 500;
    font-size: 30px;
    color: var(--ink);
  }
  .supplement-note {
    position: absolute;
    left: 0;
    width: 100%;
    top: 748px;
    text-align: center;
    font-weight: 600;
    font-size: 26px;
    letter-spacing: 6px;
    color: var(--ink);
  }
</style>
</head>
<body>
<div class="canvas">
  <section class="label">
    <svg class="label-art" width="880" height="820" viewBox="0 0 880 820" aria-hidden="true">
      <defs>
        <linearGradient id="greenField" x1="0" y1="1" x2="1" y2="0">
          <stop offset="0" stop-color="#9fc24a"/>
          <stop offset="0.6" stop-color="#b3cf5a"/>
          <stop offset="1" stop-color="#8ea540"/>
        </linearGradient>
        <linearGradient id="goldStroke" x1="0" y1="0" x2="1" y2="0">
          <stop offset="0" stop-color="#9a6f12"/>
          <stop offset="0.45" stop-color="#f2de7a"/>
          <stop offset="0.75" stop-color="#c9a227"/>
          <stop offset="1" stop-color="#9a6f12"/>
        </linearGradient>
      </defs>
      <path class="green-sweep" d="M0,660 C480,650 880,510 900,0 L880,0 L880,820 L0,820 Z" fill="url(#greenField)"/>
      <path class="white-gap" d="M0,652 C480,642 872,502 892,0" fill="none" stroke="#ffffff" stroke-width="8"/>
      <path class="gold-sweep" d="M0,644 C480,634 864,494 884,0" fill="none" stroke="url(#goldStroke)" stroke-width="7"/>
      <line class="gold-band" x1="0" y1="710" x2="880" y2="710" stroke="url(#goldStroke)" stroke-width="4"/>
    </svg>

    <div class="brand">
      <span class="brand-dot"></span>
      <span class="brand-name">Haus Solvarin</span>
    </div>

    <div class="product-title">
      <span class="title-vitamin">VITAMIN</span><span class="title-k2">K2</span>
    </div>
    <div class="title-rule"></div>
    <div class="title-form">MK-7</div>

    <div class="source">FROM NATTO EXTRACT</div>
    <div class="dose">100 MCG</div>

    <div class="free-claim">
      <span class="small">GLUTEN</span>
      <span class="small">&amp;WHEAT</span>
      <span class="big">FREE</span>
    </div>

    <div class="count-badge">50 VEGETABLE CAPSULES</div>
    <div class="supplement-note">DIETARY SUPPLEMENT</div>
  </section>
</div>
</body>
</html>
```